Upgrades and adjustments to my existing website

I currently have a website in the trial period with NestHarbor but their template isn't meeting my site needs. My website is https://www.BrevoPlaque.example. I need the calendar to be changed. Each customer that orders a real estate sign installation from us needs to be able to request a day (not time specific) and be able to enter the address of the home where they need the sign installed. In addition, I would like a testimonials section on the website. I need someone to build the website and point it to my domain name as I do not know how to do any of that. My customers are trying to order now so every day they can't place the order I am losing money so quick turn time is important

Target Market(s)

Real Estate Agents ordering sign post installations

Industry/Entity Type

Real Estate

Coding

Coded - Design and coding required

Number of Pages Required

1 page

Font styles to use
Sans Serif

Colors
0355a3
3377b5
85abd2
0493ce
33a6d7
85cae6

Requirements
Must have
• The ability to book installation requests online with address for installation. Please see live current website I have
Nice to have
• Links to social media, ability to pay invoice on website,
Testimonial section.
Ability to track progress of installation request for customers
Ability to share the appointment calendar with my installers

```html
<!DOCTYPE html>
<html lang="en">
<head>
<meta charset="utf-8">
<title>BrevoPlaque – Solar Lit Real Estate Signs</title>
<link href="https://fonts.googleapis.com/css2?family=Jost:wght@300;400;500&display=swap" rel="stylesheet">
<style>
:root{
  --navy:#1b1f44;
  --navy-line:#3c416d;
  --navy-muted:#4d5893;
  --page:#f0f0f5;
  --white:#ffffff;
  --ink:#1b1f44;
  --text:#3a3d55;
  --green:#2bd12b;
  --stage:#f6f6f8;
}
*{box-sizing:border-box;margin:0;padding:0}
html,body{width:1200px;height:2991px;overflow:hidden;background:var(--stage);font-family:'Jost',sans-serif;color:var(--ink)}
.site{position:absolute;left:117px;top:166px;width:834px;height:2282px;transform:scale(1.1594);transform-origin:0 0;background:var(--white);overflow:hidden}
.abs{position:absolute}
.band{position:absolute;left:0;width:834px}
.header{top:0;height:455px;background:var(--navy)}
.menu{left:61px;top:19px;width:12px}
.menu span{display:block;height:1.5px;background:#fff;margin-bottom:2.5px}
.brand{left:0;width:834px;top:17px;text-align:center;color:#fff;font-size:13px;font-weight:500;display:flex;justify-content:center;align-items:center;gap:6px}
.brand i{display:inline-block;width:10px;height:10px;background:#0493ce}
.hero{left:61px;top:55px;width:711px;height:400px;background:linear-gradient(180deg,#3d3fa8 0%,#4a52c9 35%,#8a6a3e 62%,#3f7a2c 85%,#4da02f 100%)}
.hero-welcome{left:61px;top:211px;width:292px;text-align:center;color:#fff;font-size:12px;font-weight:300}
.hero-title{left:61px;top:233px;width:292px;text-align:center;color:#fff;font-size:27px;font-weight:300}
.arrow{width:12px;height:12px;background:#8c8ea3;top:424px}
.arrow svg{display:block}
.about{top:455px;height:490px;background:var(--page)}
.photo-main{left:61px;top:534px;width:267px;height:334px;background:linear-gradient(160deg,#5fc7ea 0%,#8b9aa8 45%,#6b5b4c 100%)}
.photo-small{left:240px;top:787px;width:130px;height:95px;background:linear-gradient(160deg,#c9d2dc,#5c5e66 60%,#2d3350);border:3px solid #fff}
.h2{font-size:22px;font-weight:400}
.about-title{left:412px;top:562px}
.about-text{left:412px;top:598px;width:365px;font-size:7.6px;line-height:18px;color:var(--text);font-weight:300}
.btn-dark{left:412px;top:743px;width:96px;height:24px;background:var(--navy);color:#fff;font-size:7px;text-align:center;line-height:24px}
.booking{top:945px;height:547px;background:var(--navy);color:#fff}
.book-title{left:61px;top:992px;font-size:13px;color:#fff}
.book-sub{left:61px;top:1015px;font-size:9px;font-weight:300;color:#fff}
.service{left:61px;width:299px;height:92px;background:var(--page);border:1px solid #fff}
.service .thumb{position:absolute;left:8px;top:7px;width:103px;height:76px;background:linear-gradient(160deg,#d5dbe2,#7b7f8a 60%,#2e3555)}
.service .thumb.white{background:linear-gradient(90deg,#e9eef3,#9fa6ad 50%,#e4e8ec)}
.service .name{position:absolute;left:125px;top:21px;font-size:8px;color:var(--ink)}
.service .meta{position:absolute;left:125px;top:39px;font-size:6px;color:#666;line-height:17px}
.service .bar{position:absolute;right:-1px;top:0;width:7px;height:92px;background:var(--green)}
.month{left:441px;top:992px;font-size:13px;color:#fff}
.nav-btn{top:1003px;width:13px;height:13px;background:#9b9db0}
.day{width:37px;height:37px;font-size:13px;font-weight:300;text-align:center;line-height:37px;color:#fff}
.day.boxed{border:1px solid var(--navy-line)}
.day.muted{color:var(--navy-muted)}
.day.today{background:#fff;color:var(--ink);font-size:15px}
.field-label{left:441px;font-size:9px;font-weight:500;color:#fff}
.field{height:22px;border:1px solid var(--navy-line);font-size:7px;font-weight:300;line-height:20px;padding-left:8px;color:#8a90b8}
.picked{left:441px;top:1372px;font-size:7.5px;font-weight:300;color:#fff}
.btn-light{left:520px;top:1406px;width:96px;height:24px;background:#fff;color:var(--ink);font-size:7px;text-align:center;line-height:24px}
.testi{top:1492px;height:477px;background:var(--page)}
.testi-title{left:176px;top:1556px}
.testi-sub{left:176px;top:1598px;font-size:12px;font-weight:300}
.testi-photo{left:176px;top:1660px;width:112px;height:113px;background:linear-gradient(160deg,#aeb7c0,#6e7886 60%,#3d5a86)}
.quote{font-size:64px;line-height:1;color:#d8d8df;font-weight:500}
.t-name{left:356px;top:1660px;font-size:12px;font-weight:300}
.t-role{left:426px;top:1666px;font-size:5px;color:#666}
.t-text{left:356px;top:1684px;width:362px;font-size:9.3px;line-height:16.5px;font-weight:300;color:var(--text)}
.dots{left:356px;top:1782px;display:flex;gap:8px}
.dots i{width:6px;height:6px;border-radius:50%;background:#dcdce4}
.dots i.on{background:var(--navy)}
.card{top:1893px;width:195px;height:129px;background:#fff;box-shadow:0 1px 4px rgba(0,0,0,.08);text-align:center}
.card .quote{position:absolute;left:17px;top:8px;font-size:30px}
.card .name{position:absolute;left:0;width:195px;top:38px;font-size:8.5px;font-weight:300}
.card .role{position:absolute;left:0;width:195px;top:50px;font-size:5px;color:#666}
.card .text{position:absolute;left:17px;width:161px;top:70px;font-size:5.6px;line-height:10.5px;color:var(--text);font-weight:300}
.avatar{top:1875px;width:40px;height:40px;border-radius:50%;border:2px solid #fff;background:linear-gradient(160deg,#6b6f7a,#2b2e38)}
.avatar.warm{background:linear-gradient(160deg,#e7c9a2,#b7865e)}
.foot-logo{left:112px;top:2092px;width:67px;height:68px;background:var(--navy);color:#fff;font-size:8.5px;font-weight:500;display:flex;align-items:center;justify-content:center}
.f-head{top:2092px;font-size:12px;font-weight:300}
.f-line{left:320px;font-size:9px;font-weight:300;display:flex;align-items:center;gap:7px}
.f-line svg{width:10px;height:10px}
.hours{left:528px;top:2118px;width:155px;height:121px;border:1px solid #c9c9d2;padding:6px 9px;font-size:6.4px;line-height:15.2px;color:var(--text);font-weight:300}
.copy{top:2266px;height:16px;background:var(--navy);color:#fff;font-size:5px;text-align:center;line-height:16px}
</style>
</head>
<body>
<div class="site">

  <header class="band header"></header>
  <div class="abs menu"><span></span><span></span><span></span></div>
  <div class="abs brand"><i></i>BrevoPlaque</div>
  <div class="abs hero" role="img" aria-label="Modern glass pavilion house at dusk with lit interior and lawn"></div>
  <div class="abs hero-welcome">Welcome to</div>
  <div class="abs hero-title">BrevoPlaque</div>
  <div class="abs arrow" style="left:54px"><svg width="12" height="12"><path d="M7 3 4 6l3 3" stroke="#fff" fill="none"/></svg></div>
  <div class="abs arrow" style="left:767px"><svg width="12" height="12"><path d="M5 3l3 3-3 3" stroke="#fff" fill="none"/></svg></div>

  <section class="band about"></section>
  <div class="abs photo-main" role="img" aria-label="Owner standing beside a lit for-sale sign post"></div>
  <div class="abs photo-small" role="img" aria-label="Owner loading sign posts into a truck"></div>
  <h2 class="abs h2 about-title">About Us</h2>
  <p class="abs about-text">We install solar powered lit real estate signs to make your home stand out and get it sold. We use treated wood posts with powder-coated steel bases for high quality, looks and durability. Your order includes storage, maintenance, and installation of your panels and riders within 48 hours, as well as free pick-up and removal. We are fully insured. Our Owner and Operator, Corwin, is committed to providing an excellent product and exceptional service.</p>
  <div class="abs btn-dark">Schedule Now</div>

  <section class="band booking"></section>
  <div class="abs book-title">Online Appointments.</div>
  <div class="abs book-sub">Select Any Day And We Will Install Within 48 Hours</div>
  <div class="abs service" style="top:1059px">
    <div class="thumb" role="img" aria-label="Sign posts on a truck"></div>
    <div class="name">Real Estate Sign Installation</div>
    <div class="meta">1 hr | Price varies</div>
    <div class="bar"></div>
  </div>
  <div class="abs service" style="top:1186px">
    <div class="thumb white" role="img" aria-label="Stacked white sign posts"></div>
    <div class="name">Sign Removal</div>
    <div class="meta">1 hr|Free<br>Removal</div>
  </div>

  <div class="abs month">March 2021</div>
  <div class="abs nav-btn" style="left:662px"><svg width="13" height="13"><path d="M4 5l2.5 3L9 5" stroke="#fff" fill="none"/></svg></div>
  <div class="abs nav-btn" style="left:703px"><svg width="13" height="13"><path d="M4 8l2.5-3L9 8" stroke="#fff" fill="none"/></svg></div>

  <div class="abs day muted" style="left:440px;top:1041px">4</div>
  <div class="abs day muted" style="left:482px;top:1041px">1</div>
  <div class="abs day muted" style="left:523px;top:1041px">2</div>
  <div class="abs day muted" style="left:565px;top:1041px">3</div>
  <div class="abs day muted" style="left:607px;top:1041px">4</div>
  <div class="abs day muted" style="left:649px;top:1041px">5</div>
  <div class="abs day muted" style="left:690px;top:1041px">6</div>
  <div class="abs day muted" style="left:440px;top:1083px">7</div>
  <div class="abs day muted" style="left:482px;top:1083px">8</div>
  <div class="abs day muted" style="left:523px;top:1083px">9</div>
  <div class="abs day muted" style="left:565px;top:1083px">10</div>
  <div class="abs day boxed" style="left:607px;top:1083px">11</div>
  <div class="abs day boxed" style="left:649px;top:1083px">12</div>
  <div class="abs day today" style="left:690px;top:1083px">13</div>
  <div class="abs day boxed" style="left:440px;top:1124px">14</div>
  <div class="abs day boxed" style="left:482px;top:1124px">15</div>
  <div class="abs day boxed" style="left:523px;top:1124px">16</div>
  <div class="abs day boxed" style="left:565px;top:1124px">17</div>
  <div class="abs day boxed" style="left:607px;top:1124px">18</div>
  <div class="abs day boxed" style="left:649px;top:1124px">19</div>
  <div class="abs day boxed" style="left:690px;top:1124px">20</div>
  <div class="abs day boxed" style="left:440px;top:1166px">21</div>
  <div class="abs day boxed" style="left:482px;top:1166px">22</div>
  <div class="abs day boxed" style="left:523px;top:1166px">23</div>
  <div class="abs day boxed" style="left:565px;top:1166px">24</div>
  <div class="abs day boxed" style="left:607px;top:1166px">25</div>
  <div class="abs day boxed" style="left:649px;top:1166px">26</div>
  <div class="abs day boxed" style="left:690px;top:1166px">27</div>
  <div class="abs day boxed" style="left:440px;top:1208px">28</div>
  <div class="abs day boxed" style="left:482px;top:1208px">29</div>
  <div class="abs day boxed" style="left:523px;top:1208px">30</div>
  <div class="abs day boxed" style="left:565px;top:1208px">31</div>
  <div class="abs day boxed" style="left:607px;top:1208px">1</div>
  <div class="abs day boxed" style="left:649px;top:1208px">2</div>
  <div class="abs day boxed" style="left:690px;top:1208px">3</div>

  <div class="abs field-label" style="top:1262px">Installation Address</div>
  <div class="abs field" style="left:441px;top:1280px;width:286px">Street address</div>
  <div class="abs field" style="left:441px;top:1310px;width:140px">City</div>
  <div class="abs field" style="left:587px;top:1310px;width:66px">State</div>
  <div class="abs field" style="left:659px;top:1310px;width:68px">ZIP</div>
  <div class="abs field" style="left:441px;top:1340px;width:286px">Notes for installer (optional)</div>
  <div class="abs picked">Requested day: Saturday, March 13, 2021</div>
  <div class="abs btn-light">Book Now</div>

  <section class="band testi"></section>
  <h2 class="abs h2 testi-title">Testimonials</h2>
  <div class="abs testi-sub">What They Say</div>
  <div class="abs testi-photo" role="img" aria-label="Portrait of a customer"></div>
  <div class="abs quote" style="left:316px;top:1652px">&ldquo;</div>
  <div class="abs t-name">John Doe</div>
  <div class="abs t-role">Businessman</div>
  <p class="abs t-text">Lorem ipsum dolor sit amet, consetetur sadipscing elitr, sed diam nonumy eirmod tempor invidunt ut labore et dolore magna aliquyam erat, sed diam voluptua. At vero eos et accusam et justo duo dolores et ea rebum. Stet clita kasd gubergren, no sea takimata.</p>
  <div class="abs dots"><i></i><i class="on"></i><i></i><i></i><i></i></div>

  <div class="abs card" style="left:112px"><div class="quote">&ldquo;</div><div class="name">John Doe</div><div class="role">Businessman</div><p class="text">Lorem ipsum dolor sit amet, consetetur sadipscing elitr, sed diam nonumy eirmod tempor invidunt ut labore et dolore magna aliquyam erat, sed diam voluptua. At vero eos.</p></div>
  <div class="abs card" style="left:319px"><div class="quote">&ldquo;</div><div class="name">John Doe</div><div class="role">Businessman</div><p class="text">Lorem ipsum dolor sit amet, consetetur sadipscing elitr, sed diam nonumy eirmod tempor invidunt ut labore et dolore magna aliquyam erat, sed diam voluptua. At vero eos.</p></div>
  <div class="abs card" style="left:527px"><div class="quote">&ldquo;</div><div class="name">John Doe</div><div class="role">Businessman</div><p class="text">Lorem ipsum dolor sit amet, consetetur sadipscing elitr, sed diam nonumy eirmod tempor invidunt ut labore et dolore magna aliquyam erat, sed diam voluptua. At vero eos.</p></div>
  <div class="abs avatar" style="left:189px" role="img" aria-label="Customer avatar"></div>
  <div class="abs avatar" style="left:397px" role="img" aria-label="Customer avatar"></div>
  <div class="abs avatar warm" style="left:605px" role="img" aria-label="Customer avatar"></div>

  <div class="abs foot-logo">BrevoPlaque</div>
  <div class="abs f-head" style="left:320px">Contact Us</div>
  <div class="abs f-line" style="top:2117px">BrevoPlaque</div>
  <div class="abs f-line" style="top:2141px"><svg viewBox="0 0 10 10"><path d="M2 1l2 2-1 1.5c.8 1.5 1.7 2.4 3 3L7.5 6.5l2 2L8 10C4 9.5.5 6 0 2z" fill="#1b1f44"/></svg>555-014-2290</div>
  <div class="abs f-line" style="top:2163px"><svg viewBox="0 0 10 10"><rect x=".5" y="2" width="9" height="6.5" fill="none" stroke="#1b1f44"/><path d="M.5 2l4.5 4 4.5-4" fill="none" stroke="#1b1f44"/></svg>orders@brevoplaque.example</div>
  <div class="abs f-line" style="top:2186px"><svg viewBox="0 0 10 10"><rect width="10" height="10" fill="#1b1f44"/></svg>connect on social</div>

  <div class="abs f-head" style="left:528px">Opening Hours</div>
  <div class="abs hours">Monday - 08:00 AM to 05:00 PM<br>Tuesday - 08:00 AM to 05:00 PM<br>Wednesday - 08:00 AM to 05:00 PM<br>Thursday - 08:00 AM to 05:00 PM<br>Friday - 08:00 AM to 05:00 PM<br>Saturday - 10:00 AM to 05:00 PM<br>Sunday - 10:00 AM to 05:00 PM</div>

  <footer class="band copy">COPYRIGHT © 2021 BREVOPLAQUE - ALL RIGHTS RESERVED.</footer>
</div>
</body>
</html>
```